Pembrook Nightclub Flyer Grand Opening

Grand Opening Teaser Flyer For Nightclub

Text for flyer:
PEMBROOK
Nightclub + Lounge
Opening Fall 2018
Downtown Sacramento
Now Hiring (All Positions)
www.pembrookvenue.example
Powered by HALM Acoustics

Email Resume to: club@pembrookvenue.example

Target Market(s)

Upscale Nightclub and Lounge

Industry/Entity Type

Night Club

Font styles to use
Sans Serif

Colors
9ccb3b
0393ce
0355a3
b2b2b2
000000

Requirements
Must have
• Vibrant colors like the flyer example, and our logo. For use on Facebook and Instagram, will be boosted as well.
Nice to have
• Something artsy like the flyer example but not required

```html
<!DOCTYPE html>
<html lang="en">
<head>
<meta charset="utf-8">
<title>Pembrook Nightclub + Lounge — Opening Flyer</title>
<link rel="stylesheet" href="https://fonts.googleapis.com/css2?family=Open+Sans:ital,wght@0,600;0,700;0,800;1,600;1,800&display=swap">
<style>
  :root {
    --stage: #f5c443;
    --night: #000000;
    --brand-green: #9ccb3b;
    --brand-sky: #0393ce;
    --brand-blue: #0355a3;
    --brand-silver: #b2b2b2;
    --ink-white: #f4f4f4;
  }
  * { margin: 0; padding: 0; box-sizing: border-box; }
  html, body { width: 1200px; height: 800px; overflow: hidden; }
  body {
    background: var(--stage);
    position: relative;
    font-family: "Open Sans", sans-serif;
  }
  .flyer {
    position: absolute;
    left: 240px; top: 40px;
    width: 720px; height: 720px;
    overflow: hidden;
    background: var(--night);
  }
  .flyer-backdrop {
    position: absolute; inset: 0;
    background:
      radial-gradient(circle at 18% 80%, rgba(156,203,59,.85) 0 3%, rgba(156,203,59,0) 7%),
      radial-gradient(circle at 84% 90%, rgba(3,147,206,.9) 0 3%, rgba(3,147,206,0) 7%),
      radial-gradient(ellipse at 62% 24%, rgba(3,147,206,.7) 0%, rgba(3,147,206,0) 34%),
      radial-gradient(ellipse at 72% 58%, rgba(156,203,59,.4) 0%, rgba(156,203,59,0) 34%),
      linear-gradient(160deg, #0355a3 0%, #06325e 28%, #000000 60%, #000000 100%);
  }
  .club-name {
    position: absolute; top: 40px; left: 0; width: 100%;
    text-align: center;
    font-weight: 800; font-size: 96px; letter-spacing: 4px; line-height: 1.15;
    color: var(--ink-white);
  }
  .club-tagline {
    position: absolute; top: 176px; left: 0; width: 100%;
    text-align: center;
    font-weight: 800; font-style: italic;
    color: var(--brand-green);
    line-height: 1.02;
    text-shadow: 3px 3px 0 var(--brand-blue);
  }
  .club-tagline .line-one { display: block; font-size: 92px; }
  .club-tagline .line-two { display: block; font-size: 92px; }
  .details {
    position: absolute; top: 396px; left: 0; width: 100%;
    text-align: center; color: var(--ink-white);
  }
  .details .opening, .details .location, .details .hiring {
    font-weight: 600; font-size: 30px; line-height: 1.3;
  }
  .details .location { color: var(--brand-silver); }
  .contact {
    margin-top: 18px;
    font-weight: 600; font-size: 20px; line-height: 1.5;
  }
  .contact .label { color: var(--brand-green); }
  .sponsor {
    margin-top: 14px;
    font-style: italic; font-weight: 600; font-size: 22px;
    color: var(--brand-silver);
  }
</style>
</head>
<body>
  <main class="flyer">
    <div class="flyer-backdrop" role="img" aria-label="Night city scene with light streaks, glowing skyscrapers and a sports car"></div>
    <h1 class="club-name">PEMBROOK</h1>
    <h2 class="club-tagline">
      <span class="line-one">Night Club</span>
      <span class="line-two">Lounge</span>
    </h2>
    <section class="details">
      <p class="opening">Opening Fall 2018</p>
      <p class="location">Downtown Sacramento</p>
      <p class="hiring">Now Hiring (All Positions)</p>
      <div class="contact">
        <p class="website">www.pembrookvenue.example</p>
        <p class="email"><span class="label">Email Resume to:</span> club@pembrookvenue.example</p>
      </div>
      <p class="sponsor">Powered by HALM Acoustics</p>
    </section>
  </main>
</body>
</html>
```